Bref créative
Business Cards and Stationary for KRVMD
Modern
Warren Fitzhugh
Managing Partner
4185 Marlow Avenue, Suite 312
San Antonio TX 78249-6172
210-555-0148 x3092
warren@kr-vmd.example
www.kr-vmd.example
Logo Details
Font: Myriad Pro
Colors
BLUE C=85 M=50 Y=0 K=0
RED C=0 M=100 Y=100 K=0
GREY C=0 M=0 Y=0 K=90
Ai Logo Files

```html
<!DOCTYPE html>
<html lang="en">
<head>
<meta charset="utf-8">
<title>KRVMD LLC — Business Card</title>
<link rel="stylesheet" href="https://fonts.googleapis.com/css2?family=Source+Sans+3:wght@400;600;700&display=swap">
<style>
  :root{
    --blue:#1a74c4;
    --blue-dark:#13599c;
    --red:#e3141b;
    --grey:#333333;
    --grey-light:#555555;
    --paper:#ffffff;
    --backdrop:#e9eaeb;
    --rule:#9a9a9a;
  }
  *{box-sizing:border-box;margin:0;padding:0}
  html,body{width:1200px;height:871px;overflow:hidden}
  body{background:var(--backdrop);font-family:"Source Sans 3",Arial,sans-serif;color:var(--grey);position:relative}

  .card{position:absolute;left:250px;width:700px;height:400px;background:var(--paper);box-shadow:0 8px 24px rgba(0,0,0,.16);overflow:hidden}
  .card-back{top:25px}
  .card-front{top:446px}

  .brand{display:flex;align-items:center;gap:12px}
  .brand-square{width:26px;height:26px;background:var(--red);flex:none}
  .brand-name{font-weight:700;color:var(--blue);letter-spacing:1px;line-height:1;white-space:nowrap}

  /* back side */
  .back-content{position:absolute;inset:0;display:flex;flex-direction:column;align-items:center;justify-content:center;gap:34px}
  .card-back .brand-name{font-size:52px}
  .back-website{font-size:16px;font-weight:600;letter-spacing:4px;color:var(--grey-light)}

  /* front side */
  .card-front .brand{position:absolute;left:185px;top:50px}
  .card-front .brand-square{width:22px;height:22px}
  .card-front .brand-name{font-size:42px}

  .person{position:absolute;right:388px;top:240px;text-align:right}
  .person-name{font-size:21px;font-weight:600;color:var(--blue);line-height:1.2;white-space:nowrap}
  .person-title{font-size:16px;font-weight:600;color:var(--grey);line-height:1.35;white-space:nowrap}

  .divider{position:absolute;left:330px;top:165px;width:1px;height:160px;background:var(--rule)}
  .details{position:absolute;left:346px;top:163px;width:300px}
  .address{font-size:14px;line-height:1.4;color:var(--grey);white-space:nowrap}
  .details-rule{height:2px;background:var(--red);margin:8px 0 9px;width:260px}
  .contact-list{list-style:none}
  .contact-list li{display:flex;align-items:center;gap:9px;font-size:14px;line-height:24px;white-space:nowrap}
  .contact-list svg{width:12px;height:12px;flex:none}

  .stripe-red{position:absolute;left:0;bottom:58px;width:100%;height:3px;background:var(--red)}
  .band{position:absolute;left:0;bottom:0;width:100%;height:53px;background:linear-gradient(180deg,var(--blue) 0%,var(--blue-dark) 100%);display:flex;align-items:center;justify-content:center}
  .website{color:#fff;font-size:16px;font-weight:600;letter-spacing:3px}
</style>
</head>
<body>
  <section class="card card-back" aria-label="Card back">
    <div class="back-content">
      <div class="brand">
        <span class="brand-square"></span>
        <span class="brand-name">KRVMD LLC</span>
      </div>
      <p class="back-website">www.kr-vmd.example</p>
    </div>
  </section>

  <section class="card card-front" aria-label="Card front">
    <div class="brand">
      <span class="brand-square"></span>
      <span class="brand-name">KRVMD LLC</span>
    </div>

    <div class="person">
      <p class="person-name">Warren Fitzhugh</p>
      <p class="person-title">Managing Partner</p>
    </div>

    <div class="divider"></div>

    <div class="details">
      <p class="address">4185 Marlow Avenue, Suite 312<br>San Antonio TX 78249-6172</p>
      <div class="details-rule"></div>
      <ul class="contact-list">
        <li>
          <svg viewBox="0 0 24 24" aria-hidden="true"><path fill="var(--red)" d="M6.6 10.8a15.1 15.1 0 0 0 6.6 6.6l2.2-2.2a1 1 0 0 1 1-.25 11.4 11.4 0 0 0 3.6.57 1 1 0 0 1 1 1V20a1 1 0 0 1-1 1A17 17 0 0 1 3 4a1 1 0 0 1 1-1h3.5a1 1 0 0 1 1 1c0 1.25.2 2.45.57 3.57a1 1 0 0 1-.25 1z"/></svg>
          210-555-0148 x3092
        </li>
        <li>
          <svg viewBox="0 0 24 24" aria-hidden="true"><rect x="6" y="1" width="12" height="22" rx="2" fill="var(--red)"/><rect x="8" y="4" width="8" height="14" fill="#fff"/><circle cx="12" cy="20.5" r="1.2" fill="#fff"/></svg>
          210-555-0163
        </li>
        <li>
          <svg viewBox="0 0 24 24" aria-hidden="true"><rect x="6" y="2" width="12" height="7" fill="var(--red)"/><rect x="2" y="9" width="20" height="10" rx="2" fill="var(--red)"/><rect x="6" y="15" width="12" height="7" fill="#fff" stroke="var(--red)" stroke-width="2"/></svg>
          866-555-0127
        </li>
        <li>
          <svg viewBox="0 0 24 24" aria-hidden="true"><rect x="2" y="5" width="20" height="14" rx="1.5" fill="var(--red)"/><path d="M3 6l9 7 9-7" fill="none" stroke="#fff" stroke-width="2"/></svg>
          warren@kr-vmd.example
        </li>
      </ul>
    </div>

    <div class="stripe-red"></div>
    <div class="band"><span class="website">www.kr-vmd.example</span></div>
  </section>
</body>
</html>
```